Stationery Design For Specialist London law firm

We have merged two firms of London lawyers to create a new firm with a new name.

The new firms name is RT Hollby. We would like to include the description Solicitors and Advocates in the design.

We need a new design for our headed paper, business cards compliment slips etc.

The image we wish to project is fresh but not gimmicky - reliable and strong but not stuffy.

We have no strong views on font or colour this really is pretty much a blank page.

Our preference is for the name to be at the top of the page

Target Market(s)

Our clients who are individuals rather than corporate and other lawyers

Industry/Entity Type

Law Firm

Requirements
Should not have
• Legal images eg scales of justice etc

Obviously nothing childish or gimmicky

```html
<!DOCTYPE html>
<html lang="en">
<head>
<meta charset="utf-8">
<title>RT Hollby — Stationery Set</title>
<link rel="stylesheet" href="https://fonts.googleapis.com/css2?family=Josefin+Slab:wght@400&family=Arimo:wght@400&display=swap">
<style>
  :root {
    --page: #ffffff;
    --paper: #fefefc;
    --taupe-light: #9e9894;
    --taupe: #948d89;
    --taupe-deep: #8e8682;
    --stripe-tone: #a49e9a;
    --ink-light: #ffffff;
    --shadow: rgba(0, 0, 0, 0.35);
  }
  * { box-sizing: border-box; margin: 0; padding: 0; }
  html, body {
    width: 1200px; height: 900px; overflow: hidden;
    background: var(--page);
  }
  .canvas { position: relative; width: 1200px; height: 900px; }

  .piece { position: absolute; box-shadow: 8px 9px 12px var(--shadow); overflow: hidden; }
  .stripe-field { position: absolute; background: var(--stripe-tone); }

  .wordmark {
    position: absolute;
    font-family: "Josefin Slab", Georgia, serif;
    font-weight: 400;
    color: var(--ink-light);
    white-space: nowrap;
    line-height: 1;
  }
  .tagline {
    position: absolute;
    font-family: "Arimo", Arial, sans-serif;
    font-weight: 400;
    color: var(--ink-light);
    white-space: nowrap;
    line-height: 1;
  }

  /* Business card — front */
  .card-front { left: 90px; top: 40px; width: 370px; height: 221px; background: var(--taupe-light); }
  .card-front .inner-band { position: absolute; left: 0; top: 45px; width: 198px; height: 134px; background: var(--taupe); }
  .card-front .stripe-top { left: 200px; top: 45px; width: 100px; height: 40px; }
  .card-front .stripe-bottom { left: 110px; top: 179px; width: 190px; height: 42px; }
  .card-front .wordmark { left: 60px; top: 84px; font-size: 58px; }
  .card-front .tagline { left: 117px; top: 145px; font-size: 11px; }

  /* Business card — back */
  .card-back { left: 190px; top: 290px; width: 376px; height: 225px; background: var(--taupe-deep); }
  .card-back .stripe-side { left: 0; top: 0; width: 66px; height: 175px; }
  .card-back .wordmark { left: 252px; top: 41px; font-size: 25px; }
  .card-back .tagline { left: 267px; top: 70px; font-size: 8px; }

  /* Letterhead */
  .letterhead { left: 640px; top: 50px; width: 479px; height: 600px; background: var(--paper); }
  .letterhead .header-band { position: absolute; left: 0; top: 0; width: 100%; height: 94px; background: var(--taupe-deep); }
  .letterhead .stripe-corner { left: 279px; top: 0; width: 200px; height: 56px; }
  .letterhead .wordmark { left: 26px; top: 28px; font-size: 44px; }
  .letterhead .tagline { left: 52px; top: 73px; font-size: 12px; }

  /* Compliment slip */
  .comp-slip { left: 100px; top: 550px; width: 690px; height: 310px; background: var(--paper); }
  .comp-slip .stripe-head { left: 0; top: 0; width: 100%; height: 40px; }
  .comp-slip .footer-band { position: absolute; left: 0; bottom: 0; width: 100%; height: 72px; background: var(--taupe-deep); }
  .comp-slip .wordmark { right: 18px; top: 248px; font-size: 40px; }
  .comp-slip .tagline { right: 36px; top: 289px; font-size: 12px; }
</style>
</head>
<body>
<main class="canvas">

  <section class="piece card-front" aria-label="Business card, front">
    <div class="inner-band"></div>
    <div class="stripe-field stripe-top" role="img" aria-label="Diagonal stripe pattern"></div>
    <div class="stripe-field stripe-bottom" role="img" aria-label="Diagonal stripe pattern"></div>
    <p class="wordmark">RT Hollby</p>
    <p class="tagline">Solicitors &amp; Advocates</p>
  </section>

  <section class="piece card-back" aria-label="Business card, back">
    <div class="stripe-field stripe-side" role="img" aria-label="Diagonal stripe pattern"></div>
    <p class="wordmark">RT Hollby</p>
    <p class="tagline">Solicitors &amp; Advocates</p>
  </section>

  <section class="piece letterhead" aria-label="Headed paper">
    <div class="header-band"></div>
    <div class="stripe-field stripe-corner" role="img" aria-label="Diagonal stripe pattern"></div>
    <p class="wordmark">RT Hollby</p>
    <p class="tagline">Solicitors &amp; Advocates</p>
  </section>

  <section class="piece comp-slip" aria-label="Compliment slip">
    <div class="stripe-field stripe-head" role="img" aria-label="Diagonal stripe pattern"></div>
    <div class="footer-band"></div>
    <p class="wordmark">RT Hollby</p>
    <p class="tagline">Solicitors &amp; Advocates</p>
  </section>

</main>
</body>
</html>
```